Nimbo37.com.au Website and company image design

We are looking for an exceptional website designer / company to work with our new Australian Hosting Company

Nimbo37 is a new Cloud Hosting company launching in Australia that provides Scalable, On Demand computing resources to the Australian Market Place. Scalable, On Demand ocmputing is a nice way of saying fully scalable / redundant Virtual Private Server.

We require a full company image to be developed along with a Logo and Website. There is scope for ongoing development (preferred) for the successful candidate.

Website developement will require extensive jQuery ability (sliders for ordering etc (see: http://www.hostara.com.au/virtual-dedicated-servers/253/xen_vps.html).

Please communicate directly with me to establish full website scope and request further documentation / content.

Target Market(s)

Website Designers, programmers, technicians and large companies

Industry/Entity Type

It Company

Requirements
Must have
• Slider ordering system such as http://www.hostara.com.au/virtual-dedicated-servers/253/xen_vps.html

Nice to have
• CMS backend system
Should not have
• Should NOT be a monster template copy!!!

```html
<!DOCTYPE html>
<html lang="en">
<head>
<meta charset="utf-8">
<title>Nimbo37 – Australian Web Hosting</title>
<link href="https://fonts.googleapis.com/css2?family=Open+Sans:ital,wght@0,400;0,600;0,700;1,400&family=Lora:ital@1&display=swap" rel="stylesheet">
<style>
:root{
  --sky-top:#a9cfe6; --sky-bottom:#c9e3f1;
  --nav-dark:#4f6f95; --nav-light:#8fb2d2;
  --brand:#1d6fa3; --teal:#1a8ab8; --red:#d4141c;
  --green-top:#8cc43c; --green-bottom:#4f9a16;
  --ink:#333; --muted:#666; --line:#cfcfcf; --panel:#eeeeee;
  --foot:#1e2a36; --foot-text:#c9d2da; --blue-btn:#1b88c9;
}
*{box-sizing:border-box;margin:0;padding:0}
html,body{width:678px;height:1200px;overflow:hidden}
body{position:relative;font-family:"Open Sans",Arial,sans-serif;color:var(--ink);
  background:linear-gradient(var(--sky-top),var(--sky-bottom) 60%,#b7d7ea)}
.abs{position:absolute}
/* top strip */
.login input{position:absolute;top:11px;height:14px;border:1px solid #ccc;font:7px "Open Sans",sans-serif;padding-left:5px;color:#888;background:#fff}
.login .btn{position:absolute;left:513px;top:11px;width:36px;height:14px;background:#f4cc17;font-size:7px;font-weight:600;text-align:center;line-height:14px;border-radius:2px}
.social{position:absolute;top:9px;width:19px;height:19px;border-radius:3px}
/* header */
.header{left:80px;top:40px;width:518px;height:45px;border-radius:6px 6px 0 0;
  background:linear-gradient(var(--nav-light),var(--nav-dark))}
.logo-tab{left:76px;top:38px;width:98px;height:46px;background:#fff;border-radius:24px 24px 6px 6px;
  font-size:17px;font-weight:700;color:var(--brand);text-align:center;line-height:58px}
.util{right:84px;top:49px;font-size:7px;color:#fff;font-weight:600}
.util b{font-size:8.5px;margin-left:4px}
.nav a{position:absolute;top:69px;font-size:8px;color:#fff;text-decoration:none}
/* main */
.main{left:80px;top:93px;width:518px;height:893px;background:#fff;border-radius:6px 6px 0 0}
.hero{left:90px;top:104px;width:498px;height:136px;background:linear-gradient(#dcefff,#bfe0f3);overflow:hidden}
.hero h1{position:absolute;left:41px;top:30px;color:var(--brand);font-size:16px;font-weight:600;line-height:22px}
.hero h1 span{font-size:19px;display:block}
.hero .quote{position:absolute;left:87px;top:93px;width:135px;height:23px;border-radius:12px;
  background:linear-gradient(var(--green-top),var(--green-bottom));color:#fff;font-size:10px;font-weight:600;text-align:center;line-height:23px}
.hero .art{position:absolute;left:320px;top:10px;width:150px;height:122px;border-radius:12px;
  background:linear-gradient(#8e9aa6,#d9eefa)}
.search{left:90px;top:240px;width:498px;height:24px;background:#3c3c3c}
.search .lbl{position:absolute;left:10px;top:6px;color:#fff;font-size:9px;font-weight:600}
.search .field{position:absolute;left:130px;top:3px;width:226px;height:18px;background:#fff;font-size:8px;color:#777;padding:4px 5px}
.search .tld{position:absolute;left:357px;top:3px;width:53px;height:18px;background:#fff;border-left:1px solid #ccc;font-size:7px;color:var(--brand);padding:4px 4px}
.search .tld svg{position:absolute;right:5px;top:7px}
.search .go{position:absolute;left:419px;top:3px;width:72px;height:18px;border-radius:4px;background:linear-gradient(#4fb0e6,#1a7fc0);color:#fff;font-size:7px;font-weight:700;text-align:center;line-height:18px}
/* left column */
.side{background:#dbeefa;border:1px solid #b9dbef}
.side h3{font-size:9.5px;font-weight:600;color:var(--brand);text-align:center}
.map{position:absolute;left:9px;top:19px;width:67px;height:63px;border-radius:8px;background:linear-gradient(#3f62b8,#2a4a9c)}
.perk{position:absolute;left:4px;width:82px;background:#fff;border:1px solid #aacde6;border-radius:3px;font-size:6px;color:var(--brand);text-align:center;line-height:8px;display:flex;align-items:center;justify-content:center}
.spam-count{position:absolute;left:5px;top:99px;width:80px;height:27px;background:#f2f2f2;border:1px solid #ccc;text-align:center;font-size:6px;color:#444}
.spam-count b{display:block;color:var(--red);font-size:8.5px}
/* product cards */
.products{left:190px;top:276px;width:398px;height:136px;border:1px solid #ddd;background:#f6f6f6;border-radius:3px}
.card{position:absolute;top:8px;width:89px;height:120px;background:#fff;border:1px solid #ddd}
.card h4{height:21px;background:linear-gradient(var(--green-top),var(--green-bottom));color:#fff;font-size:8px;font-weight:600;text-align:center;line-height:21px}
.card .price{text-align:center;font-size:6px;color:#333;margin-top:7px}
.card .price b{color:var(--red);font-size:13px;font-weight:700}
.card p{font-size:5.6px;line-height:7.5px;text-align:center;color:#444;margin-top:5px;padding:0 3px}
.card .more{position:absolute;right:0;bottom:6px;width:40px;height:11px;background:#e4e4e4;font-size:5.6px;text-align:center;line-height:11px}
.intro h2{font-size:12.5px;font-weight:400;color:var(--teal)}
.intro p{font-size:6px;line-height:9.3px;color:#555;margin-top:4px}
.section-red{color:var(--red);font-size:8px;font-weight:700}
/* builder */
.builder{left:190px;top:517px;width:298px;height:255px;background:#e7e7e7;border:1px solid #cfcfcf;border-radius:3px}
.builder .inner{position:absolute;left:6px;top:6px;width:284px;height:242px;background:#f2f2f2}
.builder h5{position:absolute;left:7px;top:10px;font-size:8.5px;font-weight:600}
.os{position:absolute;left:7px;top:30px;width:216px;height:14px;background:#fff;border:1px solid #ccc;border-radius:2px;font-size:6px;padding:3px 4px}
.os svg{position:absolute;right:5px;top:4px}
.customise{position:absolute;left:7px;top:55px;color:var(--red);font-size:6.5px;font-weight:600}
.slider{position:absolute;left:7px;width:270px}
.slider .row{display:flex;justify-content:space-between;font-size:7px;font-weight:600;padding:0 5px}
.slider .row span span{font-weight:400;color:#666}
.slider .track{position:relative;height:5px;margin-top:8px;background:#dcdcdc;border:1px solid #bbb;border-radius:3px}
.slider .knob{position:absolute;left:0;top:-4px;width:11px;height:11px;background:var(--red);border-radius:2px}
.testimonial{left:496px;top:517px;width:91px;height:190px;background:#eeeeee}
.testimonial h5{font-size:8.5px;font-weight:600;line-height:10.5px;margin:7px 20px 0 8px}
.testimonial blockquote{font-family:"Lora",Georgia,serif;font-style:italic;font-size:6.3px;line-height:10.3px;color:#666;margin:14px 8px 0}
.testimonial cite{display:block;font-style:normal;font-size:5.8px;line-height:7.5px;margin:16px 0 0 26px;color:#333}
.total{left:217px;top:777px;width:238px;height:25px;border:1px solid #ccc;background:#fff}
.total .amt{position:absolute;left:0;top:0;width:150px;height:23px;text-align:center;line-height:23px;font-size:9.5px;font-weight:600}
.total .sel{position:absolute;right:0;top:-1px;width:88px;height:25px;background:var(--red);color:#fff;font-size:7.5px;font-weight:700;line-height:25px;padding-left:4px}
.why{left:191px;top:814px;width:294px;height:156px;border:2px solid #e6e6e6;background:#fff}
.why h3{font-size:9px;font-weight:600;margin:9px 0 0 12px}
.why ul{list-style:none;margin:5px 0 0 12px}
.why li{font-size:6.5px;color:#555;height:12.8px;display:flex;align-items:center;gap:6px}
.why .reg{position:absolute;right:-5px;top:128px;width:140px;height:19px;background:var(--blue-btn);color:#fff;font-size:6.5px;font-weight:600;text-align:center;line-height:19px}
.partners{left:84px;top:987px;width:510px;height:70px;background:linear-gradient(#fff,#e3e3e3)}
.badge{position:absolute;top:22px;height:24px;background:#c8ccd2;border-radius:3px}
/* footer */
.footer{left:80px;top:1057px;width:518px;height:143px;background:var(--foot)}
.fcol{position:absolute;top:10px;font-size:5.6px;color:var(--foot-text);line-height:9.6px}
.fcol h6{font-size:7px;color:#fff;font-weight:700;margin-bottom:5px}
.fsoc{display:flex;align-items:center;gap:5px;height:22px}
.fsoc i{width:17px;height:17px;border-radius:2px;display:block}
.flogo{position:absolute;left:397px;top:82px;font-size:13px;font-weight:700;color:#fff}
.fcopy{position:absolute;left:397px;top:117px;font-size:5.6px;color:var(--foot-text);line-height:10px}
.fcopy a{color:#6ab7ea;font-weight:600;text-decoration:none}
</style>
</head>
<body>
<div class="login">
  <input class="abs" style="left:315px;width:94px" value="username" aria-label="username">
  <input class="abs" style="left:414px;width:95px" value="password" aria-label="password">
  <div class="btn">LOGIN</div>
</div>
<span class="social" style="left:558px;background:#3fb0e8" aria-label="Chirper"></span>
<span class="social" style="left:580px;background:#3d5a98" aria-label="Facepage"></span>

<div class="abs header"></div>
<div class="abs logo-tab">Nimbo37</div>
<div class="abs util">Home &nbsp;|&nbsp; Support &nbsp;|&nbsp; Contact us <b>+1300 55 0199</b></div>
<nav class="nav">
  <a style="left:185px">Domains</a><a style="left:235px">Web Hosting</a><a style="left:300px">Virtual Servers</a>
  <a style="left:372px">Dedicated Servers</a><a style="left:457px">Resellers</a><a style="left:507px">About Us</a><a style="left:561px">Support</a>
</nav>

<div class="abs main"></div>
<section class="abs hero">
  <h1>Lorem ipsum dolor sit amet<span>Suspendisse quis tortor</span></h1>
  <div class="quote">Request a quote now!</div>
  <div class="art" role="img" aria-label="Stack of rack servers resting on a cloud"></div>
</section>
<div class="abs search">
  <span class="lbl">Domain Name Search</span>
  <div class="field">www.</div>
  <div class="tld">.com.au<svg width="6" height="4"><path d="M0 0h6L3 4z" fill="#1d6fa3"/></svg></div>
  <div class="go">Check Domain</div>
</div>

<aside class="abs side" style="left:90px;top:276px;width:90px;height:214px">
  <h3 style="margin-top:6px">100% Australian</h3>
  <div class="map" role="img" aria-label="Map of Australia with the national flag"></div>
  <div class="perk" style="top:85px;height:25px">30 day money-back<br>guarantee</div>
  <div class="perk" style="top:116px;height:27px">24x7 Emergency<br>Phone Support</div>
  <div class="perk" style="top:149px;height:26px">99.9% Service Level<br>Agreement</div>
  <div class="perk" style="top:180px;height:29px">Australia's largest<br>provider of VPS<br>Servers</div>
</aside>
<aside class="abs side" style="left:90px;top:497px;width:90px;height:133px">
  <h3 style="margin-top:7px">Spam Filtering</h3>
  <svg class="abs" style="left:16px;top:24px" width="58" height="58" viewBox="0 0 58 58">
    <circle cx="29" cy="29" r="28" fill="#2a7fc6"/>
    <path d="M29 29 L56 37 A28 28 0 0 1 46 51 Z" fill="#d4141c"/>
  </svg>
  <div class="abs" style="left:0;top:86px;width:90px;text-align:center;font-size:6px;color:#333">Todays Spam vs Email</div>
  <div class="spam-count"><b>153,074</b>Spam blocked today</div>
</aside>

<section class="abs products">
  <div class="card" style="left:8px"><h4>Domain Names</h4><div class="price">from <b>$14.95</b> /year</div>
    <p>Register your domains for com.au, net.au, org.au, co.nz, .net.nz, .com, .net, org and many more</p><div class="more">More info</div></div>
  <div class="card" style="left:106px"><h4>Web Hosting</h4><div class="price">from <b>$6.95</b> /month</div>
    <p>Reseller Web Hosting<br>Winova Website Hosting<br>Lunix Website Hosting<br>FREE Application Vault<br>FREE Email/Webmail</p><div class="more">More info</div></div>
  <div class="card" style="left:204px"><h4>VPS Hosting</h4><div class="price">from <b>$9.95</b> /month</div>
    <p>Virtumax VPS<br>HyperVista VPS<br>Citra Zenith VPS<br>VirtuWare VPS<br>Plexa &amp; cControl</p><div class="more">More info</div></div>
  <div class="card" style="left:301px"><h4>Dedicated Servers</h4><div class="price">from <b>$99.95</b> /month</div>
    <p>Dale &amp; Minimicro Servers<br>Value Series Servers<br>Same Day Servers<br>Hourly Backup<br>SERVER SPECIALS</p><div class="more">More info</div></div>
</section>

<section class="abs intro" style="left:191px;top:428px;width:397px">
  <h2>Australian Web Hosting, VPS &amp; Dedicated Servers</h2>
  <p>Lorem ipsum dolor sit amet, consectetur adipisicing elit, sed do eiusmod tempor incididunt ut labore et dolore magna aliqua. Ut enim ad minim veniam, quis nostrud exercitation ullamco laboris nisi ut aliquip ex ea commodo consequat. Duis aute irure dolor in reprehenderit in voluptate velit esse cillum dolore eu fugiat nulla pariatur. Excepteur sint occaecat cupidatat non proident, sunt in culpa qui officia deserunt mollit anim id est laborum.</p>
</section>

<div class="abs section-red" style="left:191px;top:498px">Build Your Server</div>
<section class="abs builder">
  <div class="inner">
    <h5>Select your Operating System</h5>
    <div class="os">CenterOS 4<svg width="8" height="5"><path d="M0 0h8L4 5z" fill="#777"/></svg></div>
    <div class="customise">Customise your System</div>
    <div class="slider" style="top:76px"><div class="row"><span>CPU cores <span>($15.00 per Core)</span></span><span>1 Cores</span></div><div class="track"><i class="knob"></i></div></div>
    <div class="slider" style="top:110px"><div class="row"><span>Disk Space <span>($0.60 per GB)</span></span><span>25 GB</span></div><div class="track"><i class="knob"></i></div></div>
    <div class="slider" style="top:143px"><div class="row"><span>Dedicated RAM <span>($15.00 per GB)</span></span><span>.5 GB</span></div><div class="track"><i class="knob"></i></div></div>
    <div class="slider" style="top:177px"><div class="row"><span>Premium Bandwith <span>($0.70 per GB)</span></span><span>50 GB</span></div><div class="track"><i class="knob"></i></div></div>
    <div class="slider" style="top:210px"><div class="row"><span>IP Addresses <span>($3.50 per IP Address)</span></span><span>1 IP</span></div><div class="track"><i class="knob"></i></div></div>
  </div>
</section>
<aside class="abs testimonial">
  <h5>What our Customers Say...</h5>
  <blockquote>Lorem ipsum dolor sit amet, consectetur adipisicing elit, sed do eiusmod tempor incididunt ut labore et dolore magna aliqua. Ut enim ad minim veniam, quis nostrud exercitation .</blockquote>
  <cite>Avery Tolan<br>Northgate IT Pty Ltd</cite>
</aside>
<div class="abs total"><div class="amt">Monthly Price: $18.50</div><div class="sel">Select Software
  <svg width="8" height="14" style="vertical-align:middle;margin-left:2px"><path d="M1 1l6 6-6 6" stroke="#fff" stroke-width="2" fill="none"/></svg></div></div>

<section class="abs why">
  <h3>Why Choose Nimbo37 for your domain names?</h3>
  <ul>
    <li><svg width="8" height="7"><path d="M1 4l2 2 4-5" stroke="#5aa51e" stroke-width="1.8" fill="none"/></svg>Duis placerat eros ut metus suscipit non ultricies blandit.</li>
    <li><svg width="8" height="7"><path d="M1 4l2 2 4-5" stroke="#5aa51e" stroke-width="1.8" fill="none"/></svg>Nunc elementum lacus in turpis accumsan ut feugiat.</li>
    <li><svg width="8" height="7"><path d="M1 4l2 2 4-5" stroke="#5aa51e" stroke-width="1.8" fill="none"/></svg>Ut vitae velit id nisi dictum fermentum et nec arcu.</li>
    <li><svg width="8" height="7"><path d="M1 4l2 2 4-5" stroke="#5aa51e" stroke-width="1.8" fill="none"/></svg>Mauris vitae est at odio sollicitudin ultrices blandit eget.</li>
    <li><svg width="8" height="7"><path d="M1 4l2 2 4-5" stroke="#5aa51e" stroke-width="1.8" fill="none"/></svg>Morbi id risus ac nulla vehicula commodo nec eget lorem.</li>
    <li><svg width="8" height="7"><path d="M1 4l2 2 4-5" stroke="#5aa51e" stroke-width="1.8" fill="none"/></svg>Duis placerat eros ut metus suscipit non ultricies blandit.</li>
    <li><svg width="8" height="7"><path d="M1 4l2 2 4-5" stroke="#5aa51e" stroke-width="1.8" fill="none"/></svg>Nunc elementum lacus in turpis accumsan ut feugiat.</li>
    <li><svg width="8" height="7"><path d="M1 4l2 2 4-5" stroke="#5aa51e" stroke-width="1.8" fill="none"/></svg>Ut vitae velit id nisi dictum fermentum et nec arcu.</li>
  </ul>
  <div class="reg">
    <svg width="7" height="19" style="position:absolute;left:-7px;top:0"><path d="M7 0v19L0 9.5z" fill="#1b88c9"/></svg>
    REGISTER YOUR DOMAIN HERE</div>
</section>

<section class="abs partners" aria-label="Technology partners">
  <span class="badge" style="left:16px;width:42px;border-radius:50%"></span>
  <span class="badge" style="left:90px;width:34px"></span>
  <span class="badge" style="left:158px;width:52px"></span>
  <span class="badge" style="left:253px;width:44px;height:30px;top:19px;background:#6d6f72"></span>
  <span class="badge" style="left:327px;width:80px"></span>
  <span class="badge" style="left:443px;width:48px"></span>
</section>

<footer class="abs footer">
  <div class="fcol" style="left:13px"><h6>Web Hosting</h6>Winova or Lunix?<br>Lunix Hosting<br>Winova Hosting<br>SSL Certificates<br>Advanced WebMail<br>Active Spam Filtering<br>Hosting Control Panel<br>Application Vault</div>
  <div class="fcol" style="left:102px"><h6>VPS Virtual Servers</h6>Lunix VPS<br>Winova VPS<br>Winova Plexa VPS<br>Lunix Plexa VPS<br>Plexa Hosting VPS<br>cControl Virtual Servers<br>Fantasma Add-on<br>cControl VPS<br>Zenith VPS<br>HyperVista VPS</div>
  <div class="fcol" style="left:195px"><h6>Dedicated Servers</h6>Special Offers<br>Same-Day Dedicated<br>Small Business Servers<br>Medium Business Servers<br>Enterprise Servers<br>Winova Dedicated Servers<br>Backup and Recovery<br>Data Center<br>Remote Access / Reboot<br>Dedicated Server FAQ<br>Request a Quote</div>
  <div class="fcol" style="left:302px"><h6>About Nimbo37</h6>About Nimbo37<br>Partners<br>Terms of Service<br>Service Level Agreement<br>Privacy Policy<br>Refund Policy<br>Jobs @ Nimbo37<br>Contact Us</div>
  <div class="fcol" style="left:397px"><h6>Let's Be Social!</h6>
    <div class="fsoc"><i style="background:#3fb0e8"></i>Follow us on Chirper</div>
    <div class="fsoc"><i style="background:#3d5a98"></i>Become a fan on Facepage</div></div>
  <div class="flogo">Nimbo37</div>
  <div class="fcopy">© 2012 Nimbo37. All rights reserved.<br><a>Privacy</a> | <a>Sitemap</a></div>
</footer>
</body>
</html>
```